New start-up company catalog!

Heat transfer printing company. We are set to launch later this month and need a stand out catalog to wow our customers. We are a printing/manufacturing heat transfer company geared towards apparel and promotional items.

```html
<!DOCTYPE html>
<html lang="en">
<head>
<meta charset="utf-8">
<title>Nylon and Polypro Heat Transfers – Catalog Spread</title>
<link href="https://fonts.googleapis.com/css2?family=Righteous&family=Montserrat:wght@500;600;700;800&display=swap" rel="stylesheet">
<style>
:root{
  --stage:#6d6e70;
  --paper:#ffffff;
  --teal:#3cc1c3;
  --teal-light:#dff3f3;
  --navy:#2b2566;
  --purple:#6a3aa0;
  --orange:#f7a21b;
  --orange-dark:#f39200;
  --grey-soft:#cfd2d4;
  --ink:#2b2a44;
  --pink-mark:#e6007e;
  --red-stop:#e2231a;
}
*{margin:0;padding:0;box-sizing:border-box}
html,body{width:1200px;height:494px;overflow:hidden;background:var(--stage)}
body{position:relative;font-family:"Montserrat",sans-serif}

.page{position:absolute;top:45px;width:524px;height:405px;background:var(--paper);overflow:hidden}
.page--product{left:50px}
.page--pricing{left:620px}

/* ---------- product page ---------- */
.hero-teal{position:absolute;left:0;top:0}
.product-photo{position:absolute;left:28px;top:18px;width:440px;height:232px;border-radius:14px;
  background:radial-gradient(ellipse at 25% 35%,rgba(20,20,24,.75),transparent 45%),
             radial-gradient(ellipse at 50% 40%,rgba(215,35,45,.8),transparent 40%),
             radial-gradient(ellipse at 82% 70%,rgba(196,160,110,.85),transparent 35%),
             radial-gradient(ellipse at 68% 62%,rgba(90,90,95,.7),transparent 30%),
             radial-gradient(ellipse at 20% 78%,rgba(30,60,140,.7),transparent 35%)}
.hero-title{position:absolute;right:18px;top:14px;text-align:right;font-family:"Righteous",sans-serif;font-size:21px;line-height:19px;letter-spacing:1px}
.hero-title span{display:inline-block;background:var(--purple);color:var(--orange);padding:0 3px}
.hero-title .accent{color:var(--teal)}

.feature-band{position:absolute;left:12px;top:233px;width:512px;height:82px;background:linear-gradient(90deg,var(--navy),var(--purple));display:flex;align-items:center}
.feature-band h2{font-family:"Righteous",sans-serif;font-weight:400;color:#fff;font-size:17px;line-height:19px;letter-spacing:.6px;width:276px;padding-left:10px}
.feature-band p{color:var(--orange);font-weight:700;font-size:8px;line-height:10.5px;width:226px;margin-left:2px}
.option-tag{position:absolute;left:332px;top:311px;width:192px;height:17px;background:var(--teal);color:#fff;font-weight:600;font-size:8.2px;line-height:17px;padding-left:10px}

.scale{position:absolute;left:26px;width:140px}
.scale--feel{top:325px}
.scale--opacity{top:360px}
.scale h3{text-align:center;font-size:9.5px;font-weight:700;color:var(--ink);margin-bottom:2px}
.scale .track{position:relative;height:6px;background:repeating-linear-gradient(90deg,var(--grey-soft) 0 2px,transparent 2px 3.5px)}
.scale .fill{position:absolute;left:0;top:0;height:6px;width:112px;background:var(--orange)}
.scale .fill::after{content:"";position:absolute;right:-3px;top:-5px;border:3px solid transparent;border-top:4px solid var(--teal)}
.scale .ends{display:flex;justify-content:space-between;font-size:7px;font-weight:600;color:var(--ink);margin-top:3px}

.spec{position:absolute;top:334px;width:60px;text-align:center}
.spec .box{position:relative;height:43px;border:3px solid var(--orange-dark);color:var(--teal);font-weight:800;display:flex;flex-direction:column;align-items:center;justify-content:center}
.spec .box::before{content:"";position:absolute;right:-3px;top:-3px;width:14px;height:14px;background:var(--paper);border-top:3px solid var(--grey-soft);border-right:3px solid var(--grey-soft)}
.spec .box::after{content:"";position:absolute;left:-3px;bottom:-3px;width:10px;height:3px;background:var(--grey-soft)}
.spec .value{font-size:22px;line-height:20px}
.spec .unit{font-size:8px;line-height:9px}
.spec .label{margin-top:4px;font-size:9.5px;font-weight:700;color:var(--ink)}
.spec--time{left:204px}
.spec--temp{left:284px}
.spec--pressure{left:364px}
.spec--peel{left:444px}

.folio{position:absolute;bottom:0;width:14px;height:12px;background:var(--pink-mark);color:#fff;font-size:7px;font-weight:700;text-align:center;line-height:12px}
.page--product .folio{left:0}
.page--pricing .folio{right:0}

/* ---------- pricing page ---------- */
.section-bar{position:absolute;left:0;width:512px;background:linear-gradient(90deg,var(--purple),var(--navy));color:#fff;font-weight:700}
.section-bar--title{top:9px;height:21px;font-size:16px;line-height:21px;padding-left:18px}
.section-bar--essential{top:205px;height:22px;font-size:7.5px;line-height:8.5px;padding:3px 0 0 18px}
.section-bar--stretch{top:325px;height:21px;font-size:7.5px;line-height:8.5px;padding:3px 0 0 18px}

.artwork{position:absolute;left:44px;top:79px;width:102px;height:78px;border:1px dashed #9a9a9a}
.artwork .art{position:absolute;inset:8px 6px;background:linear-gradient(135deg,#2f4b8c,#6d84b8);border-radius:6px;opacity:.85}
.dim{position:absolute;font-size:7px;color:var(--ink)}
.dim--w{left:85px;top:69px}
.dim--h{left:36px;top:114px}

.price{position:absolute;border-collapse:collapse;font-size:5.4px;font-weight:700;color:var(--ink)}
.price th{background:var(--navy);color:#fff;text-align:left;padding:1px 3px;white-space:nowrap}
.price td{background:var(--teal-light);padding:.6px 3px;text-align:right;white-space:nowrap}
.price td:first-child{text-align:center}
.price tr:nth-child(odd) td{background:#c9ecec}
.price--a{left:172px;top:80px;width:142px}
.price--b{left:322px;top:80px;width:140px}
.price--c{left:172px;top:114px;width:142px}
.price--d{left:322px;top:114px;width:140px}
.price--e{left:172px;top:135px;width:142px}

.no-ganging{position:absolute;left:464px;top:147px;width:46px;text-align:center;font-size:4.5px;font-weight:700;color:var(--ink)}
.no-ganging svg{display:block;margin:3px auto 0}

.swatches{position:absolute;left:18px;display:grid;grid-template-columns:repeat(11,38.5px);column-gap:6px;row-gap:6px}
.swatches--essential{top:233px}
.swatches--stretch{top:351px}
.swatch{height:39px;color:#fff;font-size:6.3px;font-weight:600;line-height:7px;display:flex;flex-direction:column;justify-content:flex-end;padding:0 0 2px 2px}
.swatch--white{border:1px solid #333;color:#111}
</style>
</head>
<body>

<section class="page page--product">
  <svg class="hero-teal" width="524" height="300" viewBox="0 0 524 300" aria-hidden="true">
    <polygon points="0,0 450,0 0,230" fill="#3cc1c3"/>
  </svg>
  <div class="product-photo" role="img" aria-label="Product photo: umbrella, folding chair, sports duffel, cooler bag and jute tote decorated with heat-transfer logos"></div>

  <h1 class="hero-title">
    <span>NYLON AND</span><br>
    <span>POLYPRO</span><br>
    <span>HEAT</span><br>
    <span class="accent">TRANSFERS</span>
  </h1>

  <div class="feature-band">
    <h2>NYLON MATERIAL OR NON-WOVEN/ POLYPROPYLENE MATERIAL</h2>
    <p>Looking to expand your product offerings? Look no further! Our Nylon or PolyPro heat transfers are engineered to apply on temperature sensitive products. Low temperature application is quick and easy! Hot peel them in only 7 seconds!</p>
  </div>
  <div class="option-tag">1, 2, 3 Color or Unlimited color options</div>

  <div class="scale scale--feel">
    <h3>Feel</h3>
    <div class="track"><div class="fill"></div></div>
    <div class="ends"><span>Soft</span><span>Heavy</span></div>
  </div>
  <div class="scale scale--opacity">
    <h3>Opacity</h3>
    <div class="track"><div class="fill"></div></div>
    <div class="ends"><span>Transparent</span><span>Opaque</span></div>
  </div>

  <div class="spec spec--time"><div class="box"><span class="value">7</span><span class="unit">Seconds</span></div><div class="label">Time</div></div>
  <div class="spec spec--temp"><div class="box"><span class="value">325</span><span class="unit">Degrees</span></div><div class="label">Temprature</div></div>
  <div class="spec spec--pressure"><div class="box"><span class="value">60</span><span class="unit">PSI</span></div><div class="label">Pressure</div></div>
  <div class="spec spec--peel"><div class="box">
    <svg width="20" height="26" viewBox="0 0 20 26" aria-hidden="true" fill="none" stroke="#f39200" stroke-width="2" stroke-linecap="round">
      <path d="M5 24c-3-4 3-7 0-11s3-7 0-11"/><path d="M10 24c-3-4 3-7 0-11s3-7 0-11"/><path d="M15 24c-3-4 3-7 0-11s3-7 0-11"/>
    </svg></div><div class="label">Hot Peel</div></div>

  <div class="folio">#</div>
</section>

<section class="page page--pricing">
  <div class="section-bar section-bar--title">Sizing &amp; Pricing</div>

  <span class="dim dim--w">12.75"</span>
  <span class="dim dim--h">9"</span>
  <div class="artwork"><div class="art" role="img" aria-label="Sample hand-lettered slogan artwork in navy"></div></div>

  <table class="price price--a">
    <tr><th>Nylon 9x12.75</th><th>1 color</th><th>2 color</th><th>3 color</th><th>Process</th></tr>
    <tr><td>144</td><td>n/a</td><td>n/a</td><td>n/a</td><td>$ 2.18</td></tr>
    <tr><td>288</td><td>n/a</td><td>n/a</td><td>n/a</td><td>$ 1.83</td></tr>
    <tr><td>512</td><td>$ 0.59</td><td>$ 1.03</td><td>$ 1.43</td><td>$ 1.33</td></tr>
  </table>
  <table class="price price--b">
    <tr><th>Nylon 19x12.75</th><th>1 color</th><th>2 color</th><th>3 color</th><th>Process</th></tr>
    <tr><td>144</td><td>n/a</td><td>n/a</td><td>n/a</td><td>$ 3.78</td></tr>
    <tr><td>288</td><td>n/a</td><td>n/a</td><td>n/a</td><td>$ 2.83</td></tr>
    <tr><td>512</td><td>$ 0.69</td><td>$ 1.14</td><td>$ 1.73</td><td>$ 1.98</td></tr>
  </table>
  <table class="price price--c">
    <tr><th>Nylon 9x12.75</th><th>Single Image</th><th>Set-up</th></tr>
    <tr><td>1</td><td>$0.15</td><td>$ 20.00</td></tr>
  </table>
  <table class="price price--d">
    <tr><th>Nylon 12x12</th><th>Single Image</th><th>Set-up</th></tr>
    <tr><td>1</td><td>$0.20</td><td>$ 22.00</td></tr>
  </table>
  <table class="price price--e">
    <tr><th>PolyPro 9x12.75</th><th>1 color</th><th>2 color</th><th>3 color</th><th>Process</th></tr>
    <tr><td>100</td><td>$ 1.30</td><td>$ 2.05</td><td>$ 2.48</td><td>$ 2.23</td></tr>
    <tr><td>250</td><td>$ 0.57</td><td>$ 0.90</td><td>$ 1.08</td><td>$ 0.98</td></tr>
  </table>

  <div class="no-ganging">No Art Ganging
    <svg width="38" height="38" viewBox="0 0 38 38" aria-hidden="true">
      <rect x="11" y="11" width="16" height="16" fill="#f2f2f2" stroke="#bbb" stroke-width=".6"/>
      <circle cx="16" cy="16" r="2.4" fill="#5aa84a"/><circle cx="22" cy="16" r="2.4" fill="#5aa84a"/>
      <circle cx="16" cy="22" r="2.4" fill="#5aa84a"/><circle cx="22" cy="22" r="2.4" fill="#5aa84a"/>
      <circle cx="19" cy="19" r="17" fill="none" stroke="#e2231a" stroke-width="2"/>
      <line x1="7" y1="7" x2="31" y2="31" stroke="#e2231a" stroke-width="2"/>
    </svg>
  </div>

  <div class="section-bar section-bar--essential">Available Colors:<br>Essential, Nylon</div>
  <div class="swatches swatches--essential">
    <div class="swatch" style="background:#111">Black</div>
    <div class="swatch" style="background:#98a2a9">Gray<br>7543C</div>
    <div class="swatch" style="background:#8c2040">Burgundy<br>194C</div>
    <div class="swatch" style="background:#a61c2e">Red<br>187C</div>
    <div class="swatch" style="background:#c8187c">Hot Pink<br>232c</div>
    <div class="swatch" style="background:#f19ac0">Pink<br>1905C</div>
    <div class="swatch" style="background:#3b2064">Purple<br>2685C</div>
    <div class="swatch" style="background:#1e3260">Navy<br>654C</div>
    <div class="swatch" style="background:#1f3f88">Royal<br>287C</div>
    <div class="swatch" style="background:#00a6da">Columbia<br>299C</div>
    <div class="swatch" style="background:#00b4e6">Bright Blue<br>306C</div>
    <div class="swatch" style="background:#4e3328">Brown<br>476C</div>
    <div class="swatch" style="background:#1d2f27">Dark Green<br>5535C</div>
    <div class="swatch" style="background:#00843d">Kelly Green<br>348C</div>
    <div class="swatch" style="background:#8dc63f">Bright<br>Green<br>375C</div>
    <div class="swatch" style="background:#a18d48">Vegas<br>Gold<br>4505C</div>
    <div class="swatch" style="background:#c24e27">Texas<br>Orange<br>1525C</div>
    <div class="swatch" style="background:#ee4d1e">Bright<br>Orange<br>021C</div>
    <div class="swatch" style="background:#f05a22">Orange<br>172C</div>
    <div class="swatch" style="background:#fbae2a">Gold<br>1235C</div>
    <div class="swatch" style="background:#ffe000">Yellow<br>YellowC</div>
    <div class="swatch swatch--white" style="background:#fff">White</div>
  </div>

  <div class="section-bar section-bar--stretch">Available Colors:<br>Stretch</div>
  <div class="swatches swatches--stretch">
    <div class="swatch" style="background:#111">Black</div>
    <div class="swatch" style="background:#98a2a9">Gray<br>7543C</div>
    <div class="swatch" style="background:#a61c2e">Red<br>187C</div>
    <div class="swatch" style="background:#f19ac0">Pink<br>1905C</div>
    <div class="swatch" style="background:#1e3260">Navy<br>654C</div>
    <div class="swatch" style="background:#1f3f88">Royal<br>287C</div>
    <div class="swatch" style="background:#fbae2a">Gold<br>1235C</div>
    <div class="swatch" style="background:#ffe000">Yellow<br>YellowC</div>
    <div class="swatch swatch--white" style="background:#fff">White</div>
  </div>

  <div class="folio">#</div>
</section>

</body>
</html>
```